Digital Health Records Service Landing page and site

I would like a reworking of the current Wordpress website to include the new logo. LedgerNook.site.
I want a more professional and corporate looking ( less homemade) landing page. I want a robust, reliable easy to maintain theme with minimal premium plugins.
I would like to use most of the current content minus the individual pricing box and minus the video or with a section/Page I can open/add to display a video if needed.
I would like it to be easy to customise, add pages or menu items without ruining the appearance. Clean, crisp, serious but not dull.
I want clear and visible social icons at the top. A clear call to action and form.

Project budget increased to attract better designers and get better results!

Target Market(s)

Charitable, Voluntary and Social Enterprise businesses in the UK and US

Industry/Entity Type

saas to business

Coding

Coded - Design and coding required

Font styles to use
Serif
Sans Serif

Colors

Designer to choose colors to be used in the design.

Requirements
Must have
• Clean, crisp, minimal, improved testimonial section and features section and FAQ
Should not have
• Purples, Browns, dark theme, corny stock images of therapists etc. Remember this is a digital records saas and not an online therapy site. Please no medical look, no doctors, no clinics etc.

```html
<!DOCTYPE html>
<html lang="en">
<head>
<meta charset="utf-8">
<title>LedgerNook.site — Digital Records for Counsellors</title>
<link href="https://fonts.googleapis.com/css2?family=Montserrat:wght@400;500;600;700&display=swap" rel="stylesheet">
<style>
  :root {
    --backdrop: #d5e3ee;
    --page: #ffffff;
    --brand: #6396c4;
    --brand-dark: #5588b8;
    --card-foot: #6a9dca;
    --ink: #1d1d1f;
    --ink-soft: #333840;
    --muted: #8a8f96;
    --line: #6f7378;
    --card-border: #e2e6ea;
  }
  * { box-sizing: border-box; margin: 0; padding: 0; }
  html, body { width: 1200px; height: 3000px; overflow: hidden; }
  body { background: var(--backdrop); font-family: 'Montserrat', sans-serif; color: var(--ink); position: relative; }
  .site { position: absolute; left: 168px; top: 221px; width: 864px; height: 2557px; background: var(--page); box-shadow: 0 3px 8px rgba(40,60,90,.25); overflow: hidden; }
  .abs { position: absolute; }

  /* header */
  .brand-name { left: 96px; top: 14px; display: flex; align-items: center; gap: 7px; font-size: 12px; font-weight: 600; color: var(--brand); }
  .brand-name .dot { width: 12px; height: 12px; background: var(--brand); }
  .nav { top: 20px; left: 523px; font-size: 10px; font-weight: 600; }
  .nav a { position: absolute; white-space: nowrap; color: var(--ink); text-decoration: none; }
  .nav a.active { color: var(--brand); }
  .social { left: 784px; top: 19px; display: flex; gap: 6px; }
  .social span { width: 14px; height: 14px; border-radius: 50%; background: var(--brand); }

  .btn { display: flex; align-items: center; justify-content: center; background: var(--brand); color: #fff; font-size: 10px; font-weight: 600; border-radius: 2px; text-decoration: none; }

  /* hero */
  .hero-title { left: 141px; top: 130px; font-size: 25px; font-weight: 600; color: var(--brand); }
  .hero-copy { left: 141px; top: 168px; width: 265px; font-size: 12px; line-height: 14.5px; color: var(--ink-soft); }
  .hero-btn { left: 141px; top: 243px; width: 64px; height: 23px; }
  .hero-mark { left: 470px; top: 116px; width: 240px; height: 183px; display: flex; align-items: center; justify-content: center; gap: 10px; font-size: 24px; font-weight: 600; color: var(--brand); }
  .hero-mark .dot { width: 22px; height: 22px; background: var(--brand); }

  /* efficiency band */
  .band { left: 0; top: 374px; width: 864px; height: 199px; background: var(--brand); }
  .portrait { left: 123px; top: 326px; width: 227px; height: 247px; background: linear-gradient(180deg, #c9c3bd 0%, #4a4f8a 45%, #2b2f6e 100%); border-radius: 110px 110px 0 0; }
  .band-title { left: 397px; top: 416px; font-size: 20px; font-weight: 600; color: #fff; }
  .band-copy { left: 397px; top: 446px; width: 330px; font-size: 14px; line-height: 17.4px; color: #fff; }

  /* security */
  .sec-title { left: 89px; top: 726px; width: 380px; font-size: 23px; line-height: 29px; font-weight: 600; color: var(--brand); }
  .sec-copy { left: 89px; top: 800px; width: 350px; font-size: 12px; line-height: 14.3px; color: var(--ink-soft); }
  .sec-btn { left: 89px; top: 872px; width: 77px; height: 23px; }
  .laptop { left: 484px; top: 717px; width: 271px; height: 189px; background: linear-gradient(180deg, #6396c4 0%, #6396c4 82%, #9a9a9a 84%, #c4c4c4 100%); border-radius: 8px 8px 3px 3px; }

  /* testimonials */
  .reviews { left: 0; top: 1019px; width: 864px; height: 463px; background: var(--brand); }
  .reviews-title { left: 0; top: 1089px; width: 864px; text-align: center; font-size: 22px; font-weight: 600; color: #fff; }
  .review { top: 1149px; width: 144px; height: 209px; box-shadow: 0 4px 10px rgba(30,60,100,.25); }
  .review-body { height: 154px; background: #fff; padding: 9px 9px 0; }
  .stars { display: flex; gap: 1.5px; }
  .stars svg { width: 11px; height: 11px; fill: var(--brand); }
  .review-text { height: 120px; display: flex; align-items: center; font-size: 9.4px; line-height: 14.4px; color: var(--ink-soft); }
  .review-foot { height: 55px; background: var(--card-foot); display: flex; align-items: center; gap: 6px; padding: 0 10px; }
  .avatar { width: 28px; height: 28px; border-radius: 50%; background: linear-gradient(135deg, #d8cfc6, #6b5a55); flex: none; }
  .who b { display: block; font-size: 7px; font-weight: 700; color: #fff; }
  .who span { display: block; font-size: 4.5px; color: #e3edf7; }

  /* pricing */
  .price-title { left: 0; top: 1522px; width: 864px; text-align: center; font-size: 20px; font-weight: 700; }
  .price-sub { left: 0; top: 1556px; width: 864px; text-align: center; font-size: 11px; color: var(--ink-soft); }
  .save { left: 466px; top: 1623px; font-size: 7px; font-weight: 600; color: var(--brand); }
  .toggle { left: 564px; top: 1616px; width: 103px; height: 24px; border: 1px solid var(--card-border); border-radius: 12px; display: flex; align-items: center; padding: 2px; font-size: 8.5px; font-weight: 600; }
  .toggle .on { background: var(--brand); color: #fff; border-radius: 10px; width: 46px; height: 18px; display: flex; align-items: center; justify-content: center; }
  .toggle .off { color: var(--muted); flex: 1; text-align: center; }
  .plan { background: #fff; border: 1.5px solid var(--brand); border-radius: 3px; padding: 30px 8px 0; }
  .plan-flag { position: absolute; left: 0; top: 0; width: 100%; height: 16px; background: var(--brand); color: #fff; font-size: 8px; font-weight: 500; text-align: center; line-height: 16px; }
  .plan h3 { padding-left: 5px; font-size: 12px; font-weight: 600; }
  .plan .for { padding-left: 5px; margin-top: 2px; font-size: 8px; color: var(--ink-soft); }
  .plan .cost { padding-left: 5px; margin-top: 15px; font-size: 19px; font-weight: 700; }
  .plan .cost small { font-size: 6.5px; font-weight: 400; }
  .plan .btn { margin-top: 11px; height: 23px; border-radius: 0; }
  .plan .inc { padding-left: 5px; margin-top: 27px; font-size: 9px; font-weight: 500; }
  .plan ul { list-style: none; padding-left: 5px; margin-top: 5px; }
  .plan li { display: flex; align-items: center; gap: 11px; height: 24px; font-size: 8.5px; color: var(--ink-soft); }
  .plan li svg { width: 11px; height: 11px; stroke: var(--brand); fill: none; stroke-width: 1.6; }

  /* faq */
  .faq { left: 193px; top: 1655px; width: 234px; }
  .faq h3 { font-size: 12px; font-weight: 600; color: var(--ink); margin-bottom: 12px; }
  .faq-item { border-bottom: 1px solid var(--card-border); padding: 9px 0; }
  .faq-item h4 { font-size: 9px; font-weight: 600; color: var(--brand); }
  .faq-item p { margin-top: 4px; font-size: 8.5px; line-height: 12px; color: var(--ink-soft); }

  /* contact */
  .contact-title { left: 0; top: 2103px; width: 864px; text-align: center; font-size: 22px; font-weight: 600; color: var(--brand); }
  .contact-copy { left: 262px; top: 2143px; width: 340px; text-align: center; font-size: 10px; line-height: 12px; color: var(--ink-soft); }
  .contact-phone { left: 0; top: 2180px; width: 864px; text-align: center; font-size: 14.5px; font-weight: 600; color: var(--brand); }
  .field { border-bottom: 1px solid var(--line); font-size: 10px; color: var(--muted); padding-left: 6px; }
  .send { left: 385px; top: 2455px; width: 93px; height: 23px; }
</style>
</head>
<body>
<main class="site">
  <header>
    <div class="abs brand-name"><span class="dot"></span>LedgerNook.site</div>
    <nav class="abs nav">
      <a class="active" style="left:0">About</a>
      <a style="left:46px">Features</a>
      <a style="left:104px">Security</a>
      <a style="left:160px">Price</a>
      <a style="left:200px">Contact</a>
    </nav>
    <div class="abs social" aria-label="Social links">
      <span role="img" aria-label="Social profile link"></span>
      <span role="img" aria-label="Social profile link"></span>
      <span role="img" aria-label="Social profile link"></span>
    </div>
  </header>

  <section class="hero">
    <h1 class="abs hero-title">LedgerNook</h1>
    <p class="abs hero-copy">Our intuitive and therapist-designed platform is specifically tailored to meet the unique needs of counsellors and psychotherapists like you.</p>
    <a class="abs btn hero-btn">Free trial</a>
    <div class="abs hero-mark"><span class="dot"></span>LedgerNook.site</div>
  </section>

  <section class="efficiency">
    <div class="abs band"></div>
    <div class="abs portrait" role="img" aria-label="Portrait photo of a smiling team member in a navy polo shirt"></div>
    <h2 class="abs band-title">Experience Unparalleled Efficiency</h2>
    <p class="abs band-copy">Our team of experts in mental health care, psychotherapy, and counseling have poured their knowledge and experience into developing a platform that exceeds industry standards.</p>
  </section>

  <section class="security">
    <h2 class="abs sec-title">Safety and security of client data is our top priority</h2>
    <p class="abs sec-copy">Our system employs account permissions to ensure that client data can only be viewed by the relevant team members even when therapists work across different services or teams.</p>
    <a class="abs btn sec-btn">Learn more</a>
    <div class="abs laptop" role="img" aria-label="Photo of an open laptop with a blue screen"></div>
  </section>

  <section class="testimonials">
    <div class="abs reviews"></div>
    <h2 class="abs reviews-title">What our clients are saying?</h2>

    <article class="abs review" style="left:203px">
      <div class="review-body">
        <div class="stars"><svg viewBox="0 0 10 10"><path d="M5 .5l1.3 3h3.2L7 5.4l1 3.2L5 6.7 2 8.6l1-3.2L.5 3.5h3.2z"/></svg><svg viewBox="0 0 10 10"><path d="M5 .5l1.3 3h3.2L7 5.4l1 3.2L5 6.7 2 8.6l1-3.2L.5 3.5h3.2z"/></svg><svg viewBox="0 0 10 10"><path d="M5 .5l1.3 3h3.2L7 5.4l1 3.2L5 6.7 2 8.6l1-3.2L.5 3.5h3.2z"/></svg><svg viewBox="0 0 10 10"><path d="M5 .5l1.3 3h3.2L7 5.4l1 3.2L5 6.7 2 8.6l1-3.2L.5 3.5h3.2z"/></svg><svg viewBox="0 0 10 10"><path d="M5 .5l1.3 3h3.2L7 5.4l1 3.2L5 6.7 2 8.6l1-3.2L.5 3.5h3.2z"/></svg></div>
        <p class="review-text">I have been using LedgerNook for over a year now and I love it! I can't imagine life without it. It's so easy to use, and the customer service is great.</p>
      </div>
      <div class="review-foot"><div class="avatar" role="img" aria-label="Client avatar photo"></div><div class="who"><b>Kira Walden</b><span>Team Lead</span></div></div>
    </article>

    <article class="abs review" style="left:360px">
      <div class="review-body">
        <div class="stars"><svg viewBox="0 0 10 10"><path d="M5 .5l1.3 3h3.2L7 5.4l1 3.2L5 6.7 2 8.6l1-3.2L.5 3.5h3.2z"/></svg><svg viewBox="0 0 10 10"><path d="M5 .5l1.3 3h3.2L7 5.4l1 3.2L5 6.7 2 8.6l1-3.2L.5 3.5h3.2z"/></svg><svg viewBox="0 0 10 10"><path d="M5 .5l1.3 3h3.2L7 5.4l1 3.2L5 6.7 2 8.6l1-3.2L.5 3.5h3.2z"/></svg><svg viewBox="0 0 10 10"><path d="M5 .5l1.3 3h3.2L7 5.4l1 3.2L5 6.7 2 8.6l1-3.2L.5 3.5h3.2z"/></svg><svg viewBox="0 0 10 10"><path d="M5 .5l1.3 3h3.2L7 5.4l1 3.2L5 6.7 2 8.6l1-3.2L.5 3.5h3.2z"/></svg></div>
        <p class="review-text">I have tried a lot of similar softwares and LedgerNook is the best!</p>
      </div>
      <div class="review-foot"><div class="avatar" role="img" aria-label="Client avatar photo"></div><div class="who"><b>Jerome Bale</b><span>Senior Consultant</span></div></div>
    </article>

    <article class="abs review" style="left:516px">
      <div class="review-body">
        <div class="stars"><svg viewBox="0 0 10 10"><path d="M5 .5l1.3 3h3.2L7 5.4l1 3.2L5 6.7 2 8.6l1-3.2L.5 3.5h3.2z"/></svg><svg viewBox="0 0 10 10"><path d="M5 .5l1.3 3h3.2L7 5.4l1 3.2L5 6.7 2 8.6l1-3.2L.5 3.5h3.2z"/></svg><svg viewBox="0 0 10 10"><path d="M5 .5l1.3 3h3.2L7 5.4l1 3.2L5 6.7 2 8.6l1-3.2L.5 3.5h3.2z"/></svg><svg viewBox="0 0 10 10"><path d="M5 .5l1.3 3h3.2L7 5.4l1 3.2L5 6.7 2 8.6l1-3.2L.5 3.5h3.2z"/></svg><svg viewBox="0 0 10 10"><path d="M5 .5l1.3 3h3.2L7 5.4l1 3.2L5 6.7 2 8.6l1-3.2L.5 3.5h3.2z"/></svg></div>
        <p class="review-text">Would definitely recommend LedgerNook and will definitely be using it forever.</p>
      </div>
      <div class="review-foot"><div class="avatar" role="img" aria-label="Client avatar photo"></div><div class="who"><b>Shelly Shanton</b><span>Practice Lead</span></div></div>
    </article>
  </section>

  <section class="pricing">
    <h2 class="abs price-title">Streamline your teamwork. Start free.</h2>
    <p class="abs price-sub">Choose the perfect plan for your business needs</p>
    <div class="abs save">Save 16% <span style="font-weight:400">on yearly plan!</span></div>
    <div class="abs toggle"><span class="on">Yearly</span><span class="off">Monthly</span></div>

    <div class="abs faq">
      <h3>Frequently asked questions</h3>
      <div class="faq-item"><h4>Is client data stored securely?</h4><p>Yes. Records are encrypted and visible only to permitted team members.</p></div>
      <div class="faq-item"><h4>Can I try it before paying?</h4><p>Every plan starts with a free trial, no card needed.</p></div>
      <div class="faq-item"><h4>Can I add more users later?</h4><p>You can add users or teams at any time from your settings.</p></div>
      <div class="faq-item"><h4>Do you support UK and US services?</h4><p>Yes, the platform is built for charities and social enterprises in both.</p></div>
    </div>

    <article class="abs plan" style="left:437px; top:1655px; width:235px; height:359px">
      <div class="plan-flag">Most Popular</div>
      <h3>Service Plan</h3>
      <p class="for">5 users</p>
      <p class="cost">£2.21 <small>/week</small></p>
      <a class="btn">Get started</a>
      <p class="inc">All starter features, plus:</p>
      <ul>
        <li><svg viewBox="0 0 12 12"><path d="M1.5 6.5l3 3 6-7"/></svg>Unlimited Team Creation</li>
        <li><svg viewBox="0 0 12 12"><path d="M1.5 6.5l3 3 6-7"/></svg>Waiting List Management</li>
        <li><svg viewBox="0 0 12 12"><path d="M1.5 6.5l3 3 6-7"/></svg>Team Notifications</li>
        <li><svg viewBox="0 0 12 12"><path d="M1.5 6.5l3 3 6-7"/></svg>Audit and KPI Monitoring</li>
        <li><svg viewBox="0 0 12 12"><path d="M1.5 6.5l3 3 6-7"/></svg>Issue Tracking</li>
      </ul>
    </article>
  </section>

  <section class="contact">
    <h2 class="abs contact-title">Contact us</h2>
    <p class="abs contact-copy">Please feel free to send us a message to solve any doubt that you might have, we will be happy to help you.</p>
    <p class="abs contact-phone">(123) 555 0147</p>
    <div class="abs field" style="left:219px; top:2266px; width:207px; height:16px">First Name</div>
    <div class="abs field" style="left:438px; top:2266px; width:207px; height:16px">Last Name</div>
    <div class="abs field" style="left:219px; top:2314px; width:207px; height:16px">Email</div>
    <div class="abs field" style="left:438px; top:2314px; width:207px; height:16px">Phone</div>
    <div class="abs field" style="left:219px; top:2362px; width:426px; height:69px">How can we help you?</div>
    <a class="abs btn send">Send message</a>
  </section>
</main>
</body>
</html>
```